Very High End Grooming Salon needs new business card design

I need a very nice card design I am a certified Master groomer we have a very high end clients. Our color is pink but does not have to be pink. I have a logo also a mission statement .
Fluff N Fern Pet Boutique and Spa
48810 Marlow Rd
North Palm Beach fl 33471
561 904 3782
www.fluffernboutique.example
online booking available
this is our mission statement not sure it need to go on card but here it is.
Our Mission is to show respect to all animals pampering them with the same high end tailored service one would expect to receive at a day spa
as the only certified master groomer in the area we strive to put your pets best paw forward.

Industry/Entity Type

Business

```html
<!DOCTYPE html>
<html lang="en">
<head>
<meta charset="utf-8">
<title>Fluff N Fern Pet Boutique and Spa – Business Card</title>
<link rel="stylesheet" href="https://fonts.googleapis.com/css2?family=Crimson+Text:ital,wght@0,400;0,600;1,400;1,600&display=swap">
<style>
  :root {
    --magenta: #d806b0;
    --pink-soft: #f4c6ec;
    --pink-mist: #fbe6f7;
    --plum: #6a1050;
    --white: #ffffff;
    --edge: #222222;
  }
  * { box-sizing: border-box; margin: 0; padding: 0; }
  html, body { width: 999px; height: 1200px; overflow: hidden; background: var(--white); }
  body { position: relative; font-family: "Crimson Text", Georgia, serif; }

  .card {
    position: absolute;
    width: 917px;
    height: 524px;
    border: 1.5px solid var(--edge);
    background: var(--white);
    overflow: hidden;
  }
  .card--front { left: 42px; top: 25px; }
  .card--back  { left: 37px; top: 643px; }

  .card__pattern {
    position: absolute; inset: 0;
    background:
      radial-gradient(ellipse at 30% 20%, var(--pink-mist) 0%, transparent 55%),
      radial-gradient(ellipse at 80% 30%, var(--pink-mist) 0%, transparent 50%);
  }
  .card__band { position: absolute; inset: 0; width: 100%; height: 100%; }

  .brand {
    position: absolute; left: 26px; top: 16px;
    color: var(--magenta);
    font-weight: 400;
    white-space: nowrap;
    line-height: 1;
  }
  .brand__name { font-size: 62px; }
  .brand__tagline { font-size: 40px; font-variant: small-caps; letter-spacing: 1px; margin-left: 12px; }

  .mascot {
    position: absolute; left: 78px; top: 125px; width: 296px; height: 358px;
    border-radius: 46% 40% 30% 30%;
    background: radial-gradient(ellipse at 45% 40%, #f7a8ec 0%, #ec8ede 55%, rgba(246,180,236,0.6) 100%);
    border: 6px solid var(--white);
  }

  .badge {
    position: absolute; left: 772px; top: 131px; width: 100px; height: 100px;
    border-radius: 50%;
    background: var(--white);
    border: 7px solid var(--magenta);
  }

  .booking {
    position: absolute; left: 422px; top: 210px;
    font-style: italic; font-size: 24px; color: var(--plum);
    transform: rotate(-21deg);
    white-space: nowrap;
  }

  .contact {
    position: absolute; right: 30px; top: 284px;
    text-align: right; color: var(--white);
    font-style: italic; font-weight: 600; font-size: 37px; line-height: 52px;
    white-space: nowrap;
  }

  .mission {
    position: absolute; left: 25px; top: 392px; width: 840px;
    color: var(--white); font-style: italic; font-size: 27px; line-height: 35px;
  }
</style>
</head>
<body>

<section class="card card--front">
  <div class="card__pattern" role="img" aria-label="Faint pink swirl pattern background"></div>
  <svg class="card__band" viewBox="0 0 917 524" preserveAspectRatio="none" aria-hidden="true">
    <defs>
      <linearGradient id="ribbon-front" x1="0" x2="1" y1="0" y2="0">
        <stop offset="0" stop-color="#fbe0f5" stop-opacity="0.3"/>
        <stop offset="0.5" stop-color="#f4c6ec"/>
        <stop offset="1" stop-color="#f8d6f1" stop-opacity="0.6"/>
      </linearGradient>
    </defs>
    <path d="M0 300 C120 360 330 330 500 230 C640 150 780 150 917 190 L917 210 C780 178 640 180 500 260 C340 350 140 370 0 330 Z" fill="url(#ribbon-front)"/>
    <path d="M0 320 C140 370 330 360 500 262 C640 185 780 190 917 208 L917 524 L0 524 Z" fill="var(--magenta)"/>
  </svg>

  <h1 class="brand"><span class="brand__name">Fluff N Fern</span><span class="brand__tagline">Pet Boutique and Spa</span></h1>

  <div class="mascot" role="img" aria-label="Illustration of a pink groomed poodle with swirl details"></div>

  <div class="badge" role="img" aria-label="Certification seal"></div>

  <p class="booking">Online Booking Available</p>

  <address class="contact">
    48810 Marlow Rd<br>
    Willowmere Bay ME 04999<br>
    Phone: 555-904-3782<br>
    www.fluffernboutique.example
  </address>
</section>

<section class="card card--back">
  <div class="card__pattern" role="img" aria-label="Faint pink swirl pattern background"></div>
  <svg class="card__band" viewBox="0 0 917 524" preserveAspectRatio="none" aria-hidden="true">
    <defs>
      <linearGradient id="ribbon-back" x1="0" x2="1" y1="0" y2="0">
        <stop offset="0" stop-color="#f4c6ec"/>
        <stop offset="0.6" stop-color="#f8d6f1"/>
        <stop offset="1" stop-color="#fbe6f7" stop-opacity="0.5"/>
      </linearGradient>
    </defs>
    <path d="M0 180 C90 135 200 135 330 195 C520 290 720 350 917 320 L917 335 C720 362 520 310 330 218 C200 158 90 160 0 205 Z" fill="url(#ribbon-back)"/>
    <path d="M0 205 C90 178 200 178 330 228 C520 312 720 370 917 335 L917 524 L0 524 Z" fill="var(--magenta)"/>
  </svg>

  <p class="mission">Our Mission is to show respect to all animals pampering them with the same high end tailored service one would expect to receive at a day spaas the only certified master groomer in the area we strive to put your pets best paw forward.</p>
</section>

</body>
</html>
```